we need a postcard design for our new company,
Bramblewood Wedding & Events.

I have attached our logo and 2 pictures I would like to utilise on the card if poss, definately use the logo.

Requirements
Must have
• Ph no. 5382 7160 ( just the number will do)

info@bramblewoodweddingsandevents.com.au

Wedding & Event Hire /Styling all over Melbourne, South East Suburbs, The Penninsula, The Dandenongs, Phillip Island & Gippsland.

```html
<!DOCTYPE html>
<html lang="en">
<head>
<meta charset="utf-8">
<title>Bramblewood Wedding &amp; Events – Postcard</title>
<link href="https://fonts.googleapis.com/css2?family=Lobster+Two:ital,wght@0,400;0,700;1,700&family=Pinyon+Script&display=swap" rel="stylesheet">
<style>
  :root {
    --frame-red: #d8262b;
    --frame-blue: #4fb8e0;
    --cream: #f6e6cc;
    --peach: #f1d4b6;
    --rose: #eaa0b3;
    --rose-deep: #d97d98;
    --petal-white: #f8f1e2;
    --plum: #6b1a48;
    --plum-soft: #8f2d62;
    --band: rgba(255, 240, 238, 0.45);
  }
  html, body {
    margin: 0;
    width: 1200px;
    height: 900px;
    overflow: hidden;
    background: #ffffff;
  }
  .postcard {
    position: relative;
    width: 1200px;
    height: 900px;
    background: #ffffff;
  }
  .frame-outer {
    position: absolute;
    left: 8px; top: 8px; right: 8px; bottom: 8px;
    border: 8px solid var(--frame-red);
  }
  .frame-inner {
    position: absolute;
    left: 26px; top: 26px; right: 26px; bottom: 26px;
    border: 3px solid var(--frame-blue);
    overflow: hidden;
  }
  .hero-photo {
    position: absolute;
    inset: 0;
    background:
      radial-gradient(ellipse 240px 270px at 680px 520px, var(--rose-deep) 0%, var(--rose) 45%, rgba(234,160,179,0) 100%),
      radial-gradient(ellipse 260px 220px at 1020px 720px, var(--petal-white) 0%, rgba(248,241,226,0) 100%),
      radial-gradient(ellipse 200px 180px at 180px 700px, rgba(232,170,170,0.7) 0%, rgba(232,170,170,0) 100%),
      radial-gradient(ellipse 300px 240px at 900px 150px, var(--petal-white) 0%, rgba(248,241,226,0) 100%),
      linear-gradient(135deg, var(--cream) 0%, var(--peach) 55%, var(--cream) 100%);
  }
  .tagline-band {
    position: absolute;
    left: 0; right: 0;
    top: 324px;
    height: 195px;
    background: var(--band);
  }
  .service-areas {
    position: absolute;
    left: 24px; top: 30px;
    margin: 0;
    width: 800px;
    font-family: "Pinyon Script", cursive;
    font-size: 31px;
    line-height: 55px;
    color: var(--plum-soft);
  }
  .brand {
    position: absolute;
    right: 46px; top: 68px;
    display: flex;
    align-items: center;
    gap: 10px;
    font-family: "Lobster Two", cursive;
    font-weight: 700;
    font-size: 27px;
    color: var(--plum);
  }
  .brand-dot {
    width: 14px; height: 14px;
    border-radius: 50%;
    background: var(--plum);
  }
  .tagline {
    position: absolute;
    left: 236px; top: 420px;
    margin: 0;
    font-family: "Lobster Two", cursive;
    font-weight: 700;
    font-size: 54px;
    color: var(--plum);
  }
  .contact {
    position: absolute;
    left: 20px; bottom: 24px;
    margin: 0;
    font-family: "Lobster Two", cursive;
    font-weight: 700;
    font-style: italic;
    font-size: 21px;
    line-height: 27px;
    color: var(--plum);
  }
</style>
</head>
<body>
  <main class="postcard">
    <div class="frame-outer"></div>
    <div class="frame-inner">
      <div class="hero-photo" role="img" aria-label="Soft-focus photo of a pink rose with a diamond engagement ring resting on its petals, among cream roses"></div>
      <div class="tagline-band"></div>
      <p class="service-areas">Wedding &amp; Event Hire /Styling all over Melbourne, South East Suburbs, The Penninsula, The Dandenongs, Phillip Island &amp; Gippsland.</p>
      <div class="brand"><span class="brand-dot"></span>Bramblewood Weddings &amp; Events</div>
      <h1 class="tagline">make it memorable...with us</h1>
      <p class="contact">For weddings and events contact us:<br>Ph no. 5382 7160<br>info@bramblewoodweddingsandevents.com.au</p>
    </div>
  </main>
</body>
</html>
```